Kelvar Systems Sdn. Bhd. - logo/ B.Card and letter head
Kelvar Systems Sdn. Bhd.
Kelvar Systems Sdn. Bhd. - logo/ B.Card and letter head - Information Technology
Creative Brief
Professional
Daniel Loh
Director
Lot B14, Second Floor, East Block Meridian Shopping Mall, Jalan Cempaka 7/3, Taman Sri Kenari, 43200 Cheras, Selangor D.E
daniel.loh@kelvarplay.com
512863 - P
The name and designation will be updated later. Please include the font type on on the design upon confirmation of the design. KVS is Information technology which is specilaise in lottery and gaming business so the designer will think a logo for us. You need to specific to the designer that you need a logo
will be updated later when everything had been finalized.

```html
<!DOCTYPE html>
<html lang="en">
<head>
<meta charset="utf-8">
<title>Kelvar Systems Sdn. Bhd. – Stationery</title>
<link rel="stylesheet" href="https://fonts.googleapis.com/css2?family=Open+Sans:wght@400;600&family=Roboto+Condensed:wght@300;400&display=swap">
<style>
  :root {
    --backdrop: #5f6164;
    --paper: #ffffff;
    --paper-shade: #e6e7e8;
    --ink-grey: #6a6a6a;
    --ink-dark: #3b3b3b;
    --ink-light: #c9c9c9;
    --card-black: #0d0d0d;
    --card-charcoal: #4a4a4a;
  }
  * { box-sizing: border-box; margin: 0; padding: 0; }
  html, body {
    width: 1200px; height: 799px; overflow: hidden;
    background: var(--backdrop);
    font-family: "Open Sans", Arial, sans-serif;
  }
  .stationery { position: relative; width: 1200px; height: 799px; }

  .sheet, .card { position: absolute; box-shadow: 0 6px 18px rgba(0,0,0,.45); overflow: hidden; }

  /* Brand lockup: invented name set plainly in one colour and weight */
  .brand { position: absolute; text-align: right; }
  .brand-name {
    font-family: "Open Sans", Arial, sans-serif; font-weight: 400;
    line-height: 1; letter-spacing: 1px; display: block;
  }
  .brand-tagline {
    font-family: "Open Sans", Arial, sans-serif; font-weight: 400;
    margin-top: 2px; white-space: nowrap; display: block;
  }

  /* Letterhead */
  .letterhead {
    left: 48px; top: 29px; width: 485px; height: 744px;
    background: linear-gradient(180deg, var(--paper) 0%, var(--paper) 60%, var(--paper-shade) 100%);
  }
  .letterhead .brand { right: 20px; top: 12px; }
  .letterhead .brand-name { font-size: 78px; color: var(--ink-grey); }
  .letterhead .brand-tagline { font-size: 11px; color: var(--ink-grey); }
  .letterhead-footer {
    position: absolute; left: 0; right: 0; bottom: 26px;
    text-align: center; font-size: 7.5px; line-height: 1.55; color: var(--ink-dark);
  }

  /* Cards */
  .card { border-radius: 8px; }
  .card-front-light {
    left: 564px; top: 43px; width: 420px; height: 353px;
    background: linear-gradient(180deg, var(--paper) 0%, var(--paper-shade) 100%);
  }
  .card-front-dark {
    left: 744px; top: 168px; width: 408px; height: 288px;
    background: linear-gradient(200deg, var(--card-charcoal) 0%, var(--card-black) 55%);
  }
  .card-back {
    left: 636px; top: 470px; width: 432px; height: 262px;
    background: linear-gradient(180deg, var(--card-black) 0%, var(--card-charcoal) 100%);
  }

  .contact-lines {
    position: absolute; left: 24px; top: 18px;
    font-size: 7.5px; line-height: 1.6;
  }
  .contact-lines dt { display: inline-block; width: 34px; }
  .contact-lines dd { display: inline; }
  .contact-lines dd::after { content: ""; display: block; }

  .holder { position: absolute; left: 24px; }
  .holder-name {
    font-family: "Roboto Condensed", Arial, sans-serif; font-weight: 300;
    font-size: 28px; line-height: 1; white-space: nowrap;
  }
  .holder-title {
    font-family: "Roboto Condensed", Arial, sans-serif; font-weight: 300;
    font-size: 8px; text-align: right; margin-top: 2px;
  }
  .address {
    position: absolute; left: 24px; font-size: 7.5px; line-height: 1.6; font-style: normal;
  }

  .card-front-light .contact-lines,
  .card-front-light .holder,
  .card-front-light .address { color: var(--ink-dark); }
  .card-front-light .holder { top: 190px; }
  .card-front-light .address { top: 252px; }
  .card-front-light .brand { right: 16px; top: 12px; }
  .card-front-light .brand-name { font-size: 76px; color: var(--ink-grey); }
  .card-front-light .brand-tagline { font-size: 10px; color: var(--ink-grey); }

  .card-front-dark .contact-lines,
  .card-front-dark .holder,
  .card-front-dark .address { color: var(--ink-light); }
  .card-front-dark .holder { top: 146px; }
  .card-front-dark .address { top: 188px; }
  .card-front-dark .brand { right: 18px; top: 10px; }
  .card-front-dark .brand-name { font-size: 68px; color: var(--ink-light); }
  .card-front-dark .brand-tagline { font-size: 9px; color: var(--ink-light); }

  .card-back .brand { left: 50%; top: 36px; transform: translateX(-50%); text-align: center; }
  .card-back .brand-name { font-size: 120px; color: var(--ink-light); }
  .card-back .brand-tagline { font-size: 14px; color: var(--ink-light); }
</style>
</head>
<body>
<main class="stationery">

  <section class="sheet letterhead" aria-label="Letterhead">
    <div class="brand">
      <span class="brand-name">KVS</span>
      <span class="brand-tagline">Kelvar Systems Sdn. Bhd.</span>
    </div>
    <footer class="letterhead-footer">
      <p>Lot B14, Second Floor, East Block Meridian Shopping Mall, Jalan Cempaka 7/3,</p>
      <p>Taman Sri Kenari, 43200 Cheras, Selangor D.E</p>
      <p>Phone 03 - 5518 2740 &nbsp; Fax 03 - 5518 2741 &nbsp; Email daniel.loh@kelvarplay.com</p>
    </footer>
  </section>

  <section class="card card-front-light" aria-label="Business card, light">
    <dl class="contact-lines">
      <dt>Phone</dt><dd>03 - 5518 2740</dd>
      <dt>Fax</dt><dd>03 - 5518 2741</dd>
      <dt>Email</dt><dd>daniel.loh@kelvarplay.com</dd>
    </dl>
    <div class="brand">
      <span class="brand-name">KVS</span>
      <span class="brand-tagline">Kelvar Systems Sdn. Bhd.</span>
    </div>
    <div class="holder">
      <p class="holder-name">Daniel Loh</p>
      <p class="holder-title">Director</p>
    </div>
    <address class="address">
      Lot B14, Second Floor,<br>East Block Meridian Shopping Mall,<br>Jalan Cempaka 7/3,<br>Taman Sri Kenari,<br>43200 Cheras,<br>Selangor D.E
    </address>
  </section>

  <section class="card card-front-dark" aria-label="Business card, dark">
    <dl class="contact-lines">
      <dt>Phone</dt><dd>03 - 5518 2740</dd>
      <dt>Fax</dt><dd>03 - 5518 2741</dd>
      <dt>Email</dt><dd>daniel.loh@kelvarplay.com</dd>
    </dl>
    <div class="brand">
      <span class="brand-name">KVS</span>
      <span class="brand-tagline">Kelvar Systems Sdn. Bhd.</span>
    </div>
    <div class="holder">
      <p class="holder-name">Daniel Loh</p>
      <p class="holder-title">Director</p>
    </div>
    <address class="address">
      Lot B14, Second Floor,<br>East Block Meridian Shopping Mall,<br>Jalan Cempaka 7/3,<br>Taman Sri Kenari,<br>43200 Cheras,<br>Selangor D.E
    </address>
  </section>

  <section class="card card-back" aria-label="Business card, reverse">
    <div class="brand">
      <span class="brand-name">KVS</span>
      <span class="brand-tagline">Kelvar Systems Sdn. Bhd.</span>
    </div>
  </section>

</main>
</body>
</html>
```